Redesign/Facelift for Affiliate Shopping Fashion Site

We are velunix, Fashion web site from Berlin, Germany,
looking to redesign/facelift our affiliate shopping site,
http://shop.velunix.de/bekleidung,27weky56okebmq37,ec_sale,sa
(Main page view)
http://shop.velunix.de/nordwerk-seidentunika-lisel,7uox9m8zsn2bq4j0,i
(Single article view)

Altogether we want to make it more coherent, key words being
MINIMAL and STYLISH.

NOTE:
You don´t need to completely design both pages, it would be sufficient to propose a direction you would take. However, we should be able to envision the complete solution.

The solution should be similar to another comparable affiliate site,
http://www.kaufzimt.de/browse/damen-kleidung

- - General Brief:
The design should have an overall aesthetic coherence,
especially when it comes to sizes of elements
and the bars like in the side bar left, or "Zum Shop".
The solution should be done for the main page and the single article page.

- - Here are the elements in particular, and how they should be designed:
- Main Page HEADER BAR (and single article page) elements:
header bar extends across the entire width of the screen
our logo
"Shopping" text next to the logo
search form
categories "Bekleidung, Accessoires, Schmuck" etc.
Facebook and twitter buttons

- Main page SIDEBAR (left):
elements as can be seen
menu "Preis" is replaced by a price "slider" to more accurately determine
a shopping price range

- Main page PRODUCTS:
elements as can be seen
the "% discount" symbol and "Zum Shop" elements especially
should be looked at

- Main page (and single article page) FOOTER:
should extend across the entire width of the screen

- Single article page
(http://shop.velunix.de/nordwerk-seidentunika-lisel,7uox9m8zsn2bq4j0,i)
header and footer as discussed for the Main page
bars (below the article) "Ähnliche Produkte zu….", "Weitere Produkte…" should be replaced by
"lighter" solution

Thank you,
feel free to ask question if something is not clear.
Kostis

```html
<!DOCTYPE html>
<html lang="de">
<head>
<meta charset="utf-8">
<title>velunix Shopping – Sale</title>
<link rel="stylesheet" href="https://fonts.googleapis.com/css2?family=Open+Sans:wght@400;600;700&display=swap">
<style>
:root{
  --blue:#1ba8d8;
  --blue-dark:#139ccc;
  --black:#0c0c0c;
  --orange:#f26b1c;
  --text:#3a3a3a;
  --muted:#555;
  --line:#e3e3e3;
  --link:#2f8fd8;
  --white:#fff;
}
*{box-sizing:border-box;margin:0;padding:0}
html,body{width:1200px;height:1010px;overflow:hidden;background:var(--white);font-family:"Open Sans",Arial,sans-serif;color:var(--text)}
.page{position:relative;width:1200px;height:1010px;overflow:hidden}

.sidebar{position:absolute;left:129px;top:0;width:174px}
.panel-title{background:var(--blue);color:var(--white);font-size:14px;height:35px;line-height:35px;padding-left:15px}
.farbe{position:absolute;top:0;left:0;width:174px}
.swatches{position:absolute;top:44px;left:0;display:grid;grid-template-columns:repeat(5,25px);column-gap:11px;row-gap:5px}
.swatch{width:25px;height:25px}
.swatch.white{border:1px solid #ccc}
.filter{position:absolute;left:0;width:174px}
.filter .list{position:relative;margin-top:6px;height:237px;border:1px solid #f0f0f0;overflow:hidden}
.filter ul{list-style:none;padding:1px 0 0 16px;font-size:12px;line-height:18px;color:var(--text)}
.scrollbar{position:absolute;right:1px;top:0;width:15px;height:100%;background:#f1f1f1;border-left:1px solid #e6e6e6}
.scrollbar .thumb{position:absolute;left:1px;top:17px;width:12px;height:90px;background:#e2e2e2;border:1px solid #c6c6c6;border-radius:2px}
.scrollbar .up,.scrollbar .down{position:absolute;left:4px;width:0;height:0;border-left:3px solid transparent;border-right:3px solid transparent}
.scrollbar .up{top:6px;border-bottom:4px solid #444}
.scrollbar .down{bottom:6px;border-top:4px solid #444}

.grid{position:absolute;left:320px;top:-261px;display:grid;grid-template-columns:repeat(4,181px);column-gap:8.5px;row-gap:8px}
.card{width:181px;height:329px;display:flex;flex-direction:column}
.card-title{background:var(--black);color:var(--white);font-size:12px;font-weight:600;height:36px;line-height:34px;padding-left:10px}
.card-media{position:relative;height:199px;border-left:1px solid var(--line);border-right:1px solid var(--line)}
.product-visual{position:absolute;left:48px;top:10px;width:84px;height:178px;border-radius:30px 30px 14px 14px;background:linear-gradient(180deg,#e6ecef 0%,#c9dce0 28%,#b9a6c9 55%,#b5776f 80%,#d9c6c2 100%)}
.discount{position:absolute;right:7px;top:71px;background:var(--orange);color:var(--white);font-size:17px;height:31px;line-height:31px;padding:0 6px}
.price-band{background:var(--blue);height:61px;color:var(--white);padding:12px 0 0 8px;position:relative}
.price{font-size:16px;font-weight:700}
.old-price{font-size:11px;text-decoration:line-through;margin-top:1px;opacity:.95}
.shipping{position:absolute;right:12px;top:15px;font-size:12px;font-weight:600}
.shop-btn{background:var(--blue-dark);height:33px;display:flex;align-items:center;justify-content:center;gap:8px;color:var(--white);font-size:14px}

.pagination{position:absolute;left:593px;top:763px;display:flex;border:1px solid #ddd;border-radius:3px;height:28px}
.pagination span{width:27.5px;text-align:center;line-height:26px;font-size:12px;color:var(--link);border-right:1px solid #ddd}
.pagination span:last-child{border-right:none}

.disclaimer{position:absolute;left:322px;top:846px;width:730px;font-size:12px;line-height:18px;color:var(--muted)}

.footer{position:absolute;left:0;top:896px;width:1200px;height:114px;background:#0b0b0b;color:var(--white);font-size:12px;line-height:18px}
.footer .brand{position:absolute;left:131px;top:22px;font-size:22px;font-weight:700;letter-spacing:.5px;line-height:28px}
.footer .legal{position:absolute;left:131px;top:55px}
.footer nav{position:absolute;top:22px}
.footer .nav-main{left:790px}
.footer .nav-meta{left:999px}
</style>
</head>
<body>
<div class="page">

  <aside class="sidebar">
    <section class="farbe">
      <h3 class="panel-title" style="height:35px;line-height:35px;margin-top:-2px">Farbe</h3>
      <div class="swatches">
        <span class="swatch" style="background:#7a0000"></span>
        <span class="swatch" style="background:#ff0000"></span>
        <span class="swatch" style="background:#ffee00"></span>
        <span class="swatch" style="background:#4a9a5e"></span>
        <span class="swatch" style="background:#4aa5ee"></span>
        <span class="swatch" style="background:#f080e0"></span>
        <span class="swatch" style="background:#a67aec"></span>
        <span class="swatch" style="background:#cccccc"></span>
        <span class="swatch" style="background:#000000"></span>
        <span class="swatch white" style="background:#ffffff"></span>
      </div>
    </section>

    <section class="filter" style="top:117px">
      <h3 class="panel-title">Materiale</h3>
      <div class="list">
        <ul>
          <li>&nbsp;einfarbig (161847)</li><li>zweifarbig (12320)</li><li>bunt (7445)</li>
          <li>floral (6415)</li><li>gewebe (5629)</li><li>gemustert (3037)</li>
          <li>karo (2442)</li><li>transparent (1946)</li><li>bedruckt (1557)</li>
          <li>dekor (1347)</li><li>leopard (1244)</li><li>gestreift (863)</li><li>glänzend (749)</li>
        </ul>
        <div class="scrollbar"><span class="up"></span><span class="thumb"></span><span class="down"></span></div>
      </div>
    </section>

    <section class="filter" style="top:411px">
      <h3 class="panel-title">Shops</h3>
      <div class="list" style="height:225px">
        <ul>
          <li>&nbsp;lumo (729)</li><li>Haldenhaus (6747)</li><li>Shore Avenue (39)</li>
          <li>Cotelle (47)</li><li>Dress Mart (6415)</li><li>Q-Line DENIM (409)</li>
          <li>Ansichten (7)</li><li>Marèl (68)</li><li>SHOP-A-ROBE (2)</li>
          <li>ALMA (20915)</li><li>RIVAlooks (169)</li><li>Schneidler (167)</li><li>Veranesse (431)</li>
        </ul>
        <div class="scrollbar"><span class="up"></span><span class="thumb"></span><span class="down"></span></div>
      </div>
    </section>
  </aside>

  <svg width="0" height="0" style="position:absolute">
    <symbol id="cart" viewBox="0 0 22 18">
      <path d="M1 2h3l3 10h11l2-7H6" fill="none" stroke="#fff" stroke-width="1.8" stroke-linejoin="round"/>
      <path d="M8 7h10M8.8 9.5h8.5" stroke="#fff" stroke-width="1.4"/>
      <circle cx="8.5" cy="15.5" r="1.5" fill="#fff"/><circle cx="16.5" cy="15.5" r="1.5" fill="#fff"/>
    </symbol>
  </svg>

  <main class="grid">
    <!-- 12 product cards -->
    <article class="card"><div class="card-title">Druckkleid, bunt</div><div class="card-media"><div class="product-visual" role="img" aria-label="Produktfoto: bunt bedrucktes Kleid"></div><span class="discount">- 24%</span></div><div class="price-band"><div class="price">37.99 €</div><div class="old-price">49.90 €</div><span class="shipping">Versand: +5,95</span></div><div class="shop-btn"><svg width="22" height="18"><use href="#cart"/></svg>Zum Shop</div></article>
    <article class="card"><div class="card-title">Druckkleid, bunt</div><div class="card-media"><div class="product-visual" role="img" aria-label="Produktfoto: bunt bedrucktes Kleid"></div><span class="discount">- 24%</span></div><div class="price-band"><div class="price">37.99 €</div><div class="old-price">49.90 €</div><span class="shipping">Versand: +5,95</span></div><div class="shop-btn"><svg width="22" height="18"><use href="#cart"/></svg>Zum Shop</div></article>
    <article class="card"><div class="card-title">Druckkleid, bunt</div><div class="card-media"><div class="product-visual" role="img" aria-label="Produktfoto: bunt bedrucktes Kleid"></div><span class="discount">- 24%</span></div><div class="price-band"><div class="price">37.99 €</div><div class="old-price">49.90 €</div><span class="shipping">Versand: +5,95</span></div><div class="shop-btn"><svg width="22" height="18"><use href="#cart"/></svg>Zum Shop</div></article>
    <article class="card"><div class="card-title">Druckkleid, bunt</div><div class="card-media"><div class="product-visual" role="img" aria-label="Produktfoto: bunt bedrucktes Kleid"></div><span class="discount">- 24%</span></div><div class="price-band"><div class="price">37.99 €</div><div class="old-price">49.90 €</div><span class="shipping">Versand: +5,95</span></div><div class="shop-btn"><svg width="22" height="18"><use href="#cart"/></svg>Zum Shop</div></article>

    <article class="card"><div class="card-title">Druckkleid, bunt</div><div class="card-media"><div class="product-visual" role="img" aria-label="Produktfoto: bunt bedrucktes Kleid"></div><span class="discount">- 24%</span></div><div class="price-band"><div class="price">37.99 €</div><div class="old-price">49.90 €</div><span class="shipping">Versand: +5,95</span></div><div class="shop-btn"><svg width="22" height="18"><use href="#cart"/></svg>Zum Shop</div></article>
    <article class="card"><div class="card-title">Druckkleid, bunt</div><div class="card-media"><div class="product-visual" role="img" aria-label="Produktfoto: bunt bedrucktes Kleid"></div><span class="discount">- 24%</span></div><div class="price-band"><div class="price">37.99 €</div><div class="old-price">49.90 €</div><span class="shipping">Versand: +5,95</span></div><div class="shop-btn"><svg width="22" height="18"><use href="#cart"/></svg>Zum Shop</div></article>
    <article class="card"><div class="card-title">Druckkleid, bunt</div><div class="card-media"><div class="product-visual" role="img" aria-label="Produktfoto: bunt bedrucktes Kleid"></div><span class="discount">- 24%</span></div><div class="price-band"><div class="price">37.99 €</div><div class="old-price">49.90 €</div><span class="shipping">Versand: +5,95</span></div><div class="shop-btn"><svg width="22" height="18"><use href="#cart"/></svg>Zum Shop</div></article>
    <article class="card"><div class="card-title">Druckkleid, bunt</div><div class="card-media"><div class="product-visual" role="img" aria-label="Produktfoto: bunt bedrucktes Kleid"></div><span class="discount">- 24%</span></div><div class="price-band"><div class="price">37.99 €</div><div class="old-price">49.90 €</div><span class="shipping">Versand: +5,95</span></div><div class="shop-btn"><svg width="22" height="18"><use href="#cart"/></svg>Zum Shop</div></article>

    <article class="card"><div class="card-title">Druckkleid, bunt</div><div class="card-media"><div class="product-visual" role="img" aria-label="Produktfoto: bunt bedrucktes Kleid"></div><span class="discount">- 24%</span></div><div class="price-band"><div class="price">37.99 €</div><div class="old-price">49.90 €</div><span class="shipping">Versand: +5,95</span></div><div class="shop-btn"><svg width="22" height="18"><use href="#cart"/></svg>Zum Shop</div></article>
    <article class="card"><div class="card-title">Druckkleid, bunt</div><div class="card-media"><div class="product-visual" role="img" aria-label="Produktfoto: bunt bedrucktes Kleid"></div><span class="discount">- 24%</span></div><div class="price-band"><div class="price">37.99 €</div><div class="old-price">49.90 €</div><span class="shipping">Versand: +5,95</span></div><div class="shop-btn"><svg width="22" height="18"><use href="#cart"/></svg>Zum Shop</div></article>
    <article class="card"><div class="card-title">Druckkleid, bunt</div><div class="card-media"><div class="product-visual" role="img" aria-label="Produktfoto: bunt bedrucktes Kleid"></div><span class="discount">- 24%</span></div><div class="price-band"><div class="price">37.99 €</div><div class="old-price">49.90 €</div><span class="shipping">Versand: +5,95</span></div><div class="shop-btn"><svg width="22" height="18"><use href="#cart"/></svg>Zum Shop</div></article>
    <article class="card"><div class="card-title">Druckkleid, bunt</div><div class="card-media"><div class="product-visual" role="img" aria-label="Produktfoto: bunt bedrucktes Kleid"></div><span class="discount">- 24%</span></div><div class="price-band"><div class="price">37.99 €</div><div class="old-price">49.90 €</div><span class="shipping">Versand: +5,95</span></div><div class="shop-btn"><svg width="22" height="18"><use href="#cart"/></svg>Zum Shop</div></article>
  </main>

  <nav class="pagination">
    <span>«</span><span>1</span><span>2</span><span>3</span><span>4</span><span>5</span><span>»</span>
  </nav>

  <p class="disclaimer">* Alle Angaben ohne Gewähr. Preise können sich zwischenzeitlich geändert haben. Bei Sale-Produkten stellt der durchgestrichene Preis den alten Verkaufspreis dar, der rote Preis ist der neu gültige Verkaufspreis. Es gelten die AGB des jeweiligen Shops</p>

  <footer class="footer">
    <div class="brand">VELUNIX</div>
    <div class="legal">Copyright velunix 2012.<br>velunix ist nicht verantwortlich für den Inhalt externer Links.</div>
    <nav class="nav-main">Hauptmenü<br>Zum Inhalt wechseln<br>Zum sekundären Inhalt wechseln</nav>
    <nav class="nav-meta">Kontakt<br>AGB<br>Impressum</nav>
  </footer>

</div>
</body>
</html>
```